Scrap Metal Recycling

We are looking for a simple yet bold business card. We already have the logo, please see attached. Color scheme of blue, black and white or just blue and white.

```html
<!DOCTYPE html>
<html lang="en">
<head>
<meta charset="utf-8">
<title>Ridgeline Metals Inc. — Business Card</title>
<link href="https://fonts.googleapis.com/css2?family=Poppins:wght@400;600;700&display=swap" rel="stylesheet">
<style>
  :root {
    --backdrop: #1c1917;
    --card: #1b1b1b;
    --blue: #0a8db8;
    --white: #ffffff;
    --grey: #e4e4e4;
  }
  * { margin: 0; padding: 0; box-sizing: border-box; }
  html, body {
    width: 1200px; height: 842px; overflow: hidden;
    background: var(--backdrop);
    font-family: 'Poppins', sans-serif;
  }
  .stage {
    position: relative; width: 1200px; height: 842px;
  }
  .card {
    position: absolute; top: 271px;
    width: 520px; height: 300px;
    background: var(--card);
    overflow: hidden;
    box-shadow: 0 12px 30px rgba(0,0,0,0.55);
  }
  .card--back { left: 50px; }
  .card--front { left: 630px; }

  /* Back side */
  .band {
    position: absolute; left: 0; width: 100%; height: 14px;
    background: var(--blue);
  }
  .band--top { top: 0; }
  .band--bottom { bottom: 0; }
  .contact {
    position: absolute; left: 70px; top: 58px; width: 300px;
    text-align: center; color: var(--grey);
  }
  .contact__name {
    color: var(--blue); font-weight: 700; font-size: 23px;
    letter-spacing: 0.5px; line-height: 1.1; text-transform: uppercase;
  }
  .contact__role {
    font-size: 13px; letter-spacing: 0.6px; text-transform: uppercase;
    margin-top: 2px;
  }
  .divider {
    width: 62px; height: 2px; background: var(--blue);
    margin: 12px auto;
  }
  .contact__lines {
    font-size: 13.5px; line-height: 1.3; letter-spacing: 0.4px;
    text-transform: uppercase;
  }
  .contact__phone { font-size: 16px; letter-spacing: 0.8px; }

  /* Front side */
  .tab {
    position: absolute; width: 26px; background: var(--blue);
  }
  .tab--left { left: 0; top: 150px; height: 70px; }
  .tab--right { right: 0; top: 40px; height: 70px; }
  .brand {
    position: absolute; left: 0; right: 0; top: 128px;
    display: flex; align-items: center; justify-content: center; gap: 12px;
  }
  .brand__mark {
    width: 14px; height: 14px; background: var(--white);
  }
  .brand__name {
    color: var(--white); font-weight: 700; font-size: 30px;
    letter-spacing: 0.5px; text-transform: uppercase;
  }
</style>
</head>
<body>
  <main class="stage">
    <section class="card card--back" aria-label="Business card back">
      <div class="band band--top"></div>
      <div class="contact">
        <h1 class="contact__name">Marcus Delaney</h1>
        <p class="contact__role">Managing Director</p>
        <div class="divider"></div>
        <p class="contact__lines">
          <span class="contact__phone">055-284 317 602</span><br>
          hello@ridgelinemetals.com<br>
          www.ridgelinemetals.com
        </p>
        <div class="divider"></div>
        <p class="contact__lines">
          87, Foundry Road Unit 4<br>
          30918, Westland
        </p>
      </div>
      <div class="band band--bottom"></div>
    </section>

    <section class="card card--front" aria-label="Business card front">
      <div class="tab tab--right"></div>
      <div class="tab tab--left"></div>
      <div class="brand">
        <span class="brand__mark"></span>
        <span class="brand__name">Ridgeline Metals Inc.</span>
      </div>
    </section>
  </main>
</body>
</html>
```